Business Card Design Project

I need the following:

Logo -
Name - Dale Prewitt
Title - Customer Experience Officer
Web - www.bvrh.net
Phone - 555-417-3068
Updates

Project Deadline Extended
Reason: I launched the project later than anticipated. I look forward to seeing your designs. Dale

Industry/Entity Type

Business

```html
<!DOCTYPE html>
<html lang="en">
<head>
<meta charset="utf-8">
<title>Broadview Relay House – Business Cards</title>
<link rel="stylesheet" href="https://fonts.googleapis.com/css2?family=Exo+2:wght@400;600;800&display=swap">
<style>
  :root {
    --bg: #e9e7e3;
    --card-white: #ffffff;
    --card-grey: #e4e6e9;
    --blue-deep: #0a3f7a;
    --blue-mid: #1673c2;
    --blue-bright: #2aa7e8;
    --ink: #1d1d1f;
    --text-light: #ffffff;
    --shadow: rgba(0,0,0,0.18);
  }
  * { box-sizing: border-box; margin: 0; padding: 0; }
  html, body { width: 1200px; height: 899px; overflow: hidden; }
  body {
    background: var(--bg);
    font-family: "Exo 2", sans-serif;
    position: relative;
  }
  .card {
    position: absolute;
    left: 300px;
    width: 600px;
    height: 343px;
    overflow: hidden;
    box-shadow: 0 10px 24px var(--shadow);
    background: radial-gradient(ellipse at 60% 40%, var(--card-white) 0%, var(--card-grey) 100%);
  }
  .card--front { top: 81px; }
  .card--back { top: 474px; }

  /* front */
  .front-mark {
    position: absolute;
    left: 60px; top: 120px;
    display: flex; align-items: center; gap: 14px;
  }
  .mark-dot {
    width: 64px; height: 64px; border-radius: 50%;
    background: var(--blue-mid);
    flex-shrink: 0;
  }
  .mark-name {
    font-weight: 800; font-size: 46px; color: var(--blue-deep);
    letter-spacing: 1px;
  }
  .web-tab {
    position: absolute;
    right: 0; bottom: 26px;
    width: 260px; height: 34px;
    border-radius: 12px 0 0 12px;
    background: linear-gradient(90deg, var(--blue-deep), var(--blue-mid) 60%, var(--blue-deep));
    color: var(--text-light);
    font-size: 13px; letter-spacing: 2px;
    display: flex; align-items: center; padding-left: 30px;
  }

  /* back */
  .back-waves { position: absolute; inset: 0; width: 100%; height: 100%; }
  .back-brand {
    position: absolute; left: 36px; top: 52px;
    display: flex; align-items: center; gap: 14px;
  }
  .back-brand .mark-dot { width: 58px; height: 58px; }
  .brand-text { display: flex; flex-direction: column; }
  .brand-name {
    font-weight: 800; font-size: 22px; line-height: 0.98;
    color: var(--ink); text-transform: uppercase; letter-spacing: 0.5px;
  }
  .brand-web {
    margin-top: 3px; font-size: 11px; font-weight: 600; color: var(--blue-mid);
    border-top: 1.5px solid var(--blue-mid); padding-top: 2px; width: 150px;
  }
  .holder {
    position: absolute; left: 40px; top: 240px; color: var(--text-light);
  }
  .holder-name { font-size: 18px; font-weight: 600; letter-spacing: 1px; text-transform: uppercase; }
  .holder-title { font-size: 12px; letter-spacing: 1px; text-transform: uppercase; margin-top: 2px; }
  .address {
    position: absolute; left: 40px; bottom: 18px;
    color: var(--text-light); font-size: 12px; letter-spacing: 0.5px;
  }
  .contacts {
    position: absolute; right: 40px; top: 154px;
    list-style: none; color: var(--text-light);
    font-size: 13px; letter-spacing: 1px;
  }
  .contacts li { display: flex; align-items: center; gap: 8px; height: 23px; }
  .contacts svg { width: 14px; height: 14px; flex-shrink: 0; fill: none; stroke: var(--text-light); stroke-width: 1.6; }
</style>
</head>
<body>

<section class="card card--front" aria-label="Card front">
  <div class="front-mark">
    <span class="mark-dot"></span>
    <span class="mark-name">BVRH</span>
  </div>
  <div class="web-tab">www.urwebsitename.com</div>
</section>

<section class="card card--back" aria-label="Card back">
  <svg class="back-waves" viewBox="0 0 600 343" preserveAspectRatio="none">
    <defs>
      <radialGradient id="blueGlow" cx="0.55" cy="0.55" r="0.7">
        <stop offset="0" stop-color="#2aa7e8"/>
        <stop offset="0.5" stop-color="#1673c2"/>
        <stop offset="1" stop-color="#0a3f7a"/>
      </radialGradient>
    </defs>
    <path d="M0 190 C200 200 400 120 600 20 L600 343 L0 343 Z" fill="#111"/>
    <path d="M0 206 C200 216 400 136 600 36 L600 343 L0 343 Z" fill="url(#blueGlow)"/>
    <path d="M0 206 C200 216 400 136 600 36" stroke="#ffffff" stroke-width="2" fill="none" opacity="0.6"/>
  </svg>

  <div class="back-brand">
    <span class="mark-dot"></span>
    <div class="brand-text">
      <span class="brand-name">Broadview</span>
      <span class="brand-name">Relay</span>
      <span class="brand-name">House</span>
      <span class="brand-web">www.bvrh.net</span>
    </div>
  </div>

  <ul class="contacts">
    <li><svg viewBox="0 0 14 14"><path d="M3 1 L5 4 L4 6 C5 8 6 9 8 10 L10 9 L13 11 L11 13 C6 12 2 8 1 3 Z"/></svg>555-417-3068</li>
    <li><svg viewBox="0 0 14 14"><rect x="4" y="1" width="6" height="12" rx="1"/><path d="M6 11 h2"/></svg>012 345 6789</li>
    <li><svg viewBox="0 0 14 14"><rect x="2" y="6" width="10" height="7"/><rect x="4" y="1" width="6" height="5"/></svg>012 345 6789</li>
    <li><svg viewBox="0 0 14 14"><rect x="1" y="3" width="12" height="8"/><path d="M1 3 L7 8 L13 3"/></svg>urname@email.com</li>
    <li><svg viewBox="0 0 14 14"><circle cx="7" cy="7" r="6"/><path d="M1 7 h12 M7 1 C4 4 4 10 7 13 M7 1 C10 4 10 10 7 13"/></svg>www.urwebsitename.com</li>
  </ul>

  <div class="holder">
    <p class="holder-name">Dale Prewitt</p>
    <p class="holder-title">Customer Experience Officer</p>
  </div>
  <p class="address">041.12th floor,Harbor Crest Road NRV</p>
</section>

</body>
</html>
```